Dual (Twin) Wet Wipe Packaging

We are a NY Based Hygiene Brand Specifically for couples, Creating Dual products for Him and Her,
Brand Name is quelvin.
Our Initial Product is a single Wet wipe Dual Package with perforated lines one wipe for him and one for her used for after sex.
We Would like to see designs that show a bold modern design with slight edgy to bring out the fun!
The final design Should bring out the idea of couples, connection and bond,

Attached Are photos of color ideas And Attached Design ideas.

The measurement of each half should be 7*9 cm total 14*9 cm with both attached.

```html
<!DOCTYPE html>
<html lang="en">
<head>
<meta charset="utf-8">
<title>quelvin — Intimate Wipes dual sachet</title>
<link rel="stylesheet" href="https://fonts.googleapis.com/css2?family=Josefin+Sans:wght@200;300&family=Exo+2:wght@500&display=swap">
<style>
  :root {
    --stage: #2f2f2f;
    --him-deep: #1a7ee6;
    --him-mid: #2a9df0;
    --him-light: #62ccff;
    --him-ink: #ebe8e3;
    --him-tag: #2747c4;
    --her-deep: #efc2d9;
    --her-mid: #f6d6e6;
    --her-light: #fdf1f6;
    --her-ink: #731f49;
    --her-tag: #e0365f;
    --tag-ink: #ffffff;
    --teeth: 7px;
  }
  * { box-sizing: border-box; margin: 0; padding: 0; }
  html, body { width: 1200px; height: 664px; overflow: hidden; background: var(--stage); }
  .canvas { position: relative; width: 1200px; height: 664px; }

  .sachet-pair {
    position: absolute; left: 176px; top: 108px;
    width: 788px; height: 444px;
    display: flex;
  }
  .sachet {
    position: relative; width: 394px; height: 444px;
  }
  .sachet--him { background: var(--him-deep); }
  .sachet--her { background: var(--her-deep); }

  /* serrated top and bottom edges */
  .sachet::before, .sachet::after {
    content: ""; position: absolute; left: 0; right: 0; height: var(--teeth);
    background-size: calc(var(--teeth) * 2) var(--teeth);
    background-repeat: repeat-x;
  }
  .sachet::before { top: calc(var(--teeth) * -1); }
  .sachet::after { bottom: calc(var(--teeth) * -1); transform: scaleY(-1); }
  .sachet--him::before, .sachet--him::after {
    background-image:
      linear-gradient(45deg, transparent 50%, var(--him-deep) 50%),
      linear-gradient(-45deg, transparent 50%, var(--him-deep) 50%);
    background-image: linear-gradient(135deg, var(--him-deep) 25%, transparent 25%), linear-gradient(225deg, var(--him-deep) 25%, transparent 25%);
    background-position: 0 100%, 0 100%;
    background-image: conic-gradient(from 135deg at 50% 0, var(--him-deep) 90deg, transparent 0);
  }
  .sachet--her::before, .sachet--her::after {
    background-image: conic-gradient(from 135deg at 50% 0, var(--her-deep) 90deg, transparent 0);
  }
  .sachet::before { transform: scaleY(-1); }
  .sachet::after { transform: none; }

  .perforation {
    position: absolute; left: 393px; top: -7px; width: 2px; height: 458px;
    background: repeating-linear-gradient(to bottom, #2a2a2a 0 3px, transparent 3px 6px);
    opacity: .55;
  }

  .sachet__seal {
    position: absolute; inset: 0;
    border-style: solid; border-width: 34px 0 26px 30px;
  }
  .sachet--him .sachet__seal { border-color: rgba(20, 100, 215, .55); }
  .sachet--her .sachet__seal { border-color: rgba(240, 200, 222, .7); border-left-width: 30px; }

  .sachet__face {
    position: absolute; top: 34px; left: 30px; right: 0; bottom: 26px;
  }
  .sachet--him .sachet__face {
    background: linear-gradient(160deg, var(--him-deep) 0%, var(--him-mid) 45%, var(--him-light) 100%);
  }
  .sachet--her .sachet__face {
    background: linear-gradient(200deg, var(--her-deep) 0%, var(--her-mid) 45%, var(--her-light) 100%);
  }

  .sachet__content {
    position: absolute; inset: 0;
    display: flex; flex-direction: column; align-items: center;
    padding-left: 0;
  }
  .brand {
    position: absolute; top: 64px; left: 0; right: 0; text-align: center;
    font-family: "Josefin Sans", sans-serif; font-weight: 300;
    font-size: 52px; letter-spacing: -1px; line-height: 1;
  }
  .product-name {
    position: absolute; top: 180px; left: 0; right: 0; text-align: center;
    font-family: "Josefin Sans", sans-serif; font-weight: 200;
    font-size: 56px; line-height: 58px; letter-spacing: 1px;
    text-transform: uppercase;
  }
  .audience-tag {
    position: absolute; top: 359px; left: 50%; transform: translateX(-50%);
    width: 120px; height: 27px;
    display: flex; align-items: center; justify-content: center;
    font-family: "Exo 2", sans-serif; font-weight: 500;
    font-size: 15px; letter-spacing: .5px; color: var(--tag-ink);
  }

  .sachet--him .brand, .sachet--him .product-name { color: var(--him-ink); }
  .sachet--her .brand, .sachet--her .product-name { color: var(--her-ink); }
  .sachet--him .audience-tag { background: var(--him-tag); }
  .sachet--her .audience-tag { background: var(--her-tag); }
</style>
</head>
<body>
<main class="canvas">
  <section class="sachet-pair">
    <article class="sachet sachet--him">
      <div class="sachet__seal"></div>
      <div class="sachet__face" role="img" aria-label="Blue halftone dot pattern fading across the sachet"></div>
      <div class="sachet__content">
        <p class="brand">quelvin</p>
        <h2 class="product-name">Intimate<br>Wipes</h2>
        <p class="audience-tag">FOR HIM</p>
      </div>
    </article>
    <article class="sachet sachet--her">
      <div class="sachet__seal"></div>
      <div class="sachet__face" role="img" aria-label="Pink halftone dot pattern fading across the sachet"></div>
      <div class="sachet__content">
        <p class="brand">quelvin</p>
        <h2 class="product-name">Intimate<br>Wipes</h2>
        <p class="audience-tag">FOR HER</p>
      </div>
    </article>
    <div class="perforation"></div>
  </section>
</main>
</body>
</html>
```